BRANDHILL real estate family office

Hello, Our business is a real estate intermediation activity on high-end goods (amounts exceeding € 10m) for corporate and private clients. You can see our logo on the site www.brandhill-demo.fr We would like to keep that spirit with the hexagon that represents France (transactions between Monaco and Saint Tropez, Courchevel and Paris). And the "baseline" that is "real estate family office". The corporate logo should be and can be printed by embossing (relief). We must integrate the name, first name, phone, email and website. Finally, to imbibe the spirit of business, here is a detail of the activity. "Genuine consulting firm in real estate investments, BRANDHILL works with its customers as a specialized player in the high-end markets, we are recognized for our ultra-confidential approach and tailor-made, as well as the quality of our network. We broadcast any information on the market and we work exclusively through a strong relationship we have developed over the years. BRANDHILL is active on the French Riviera (from Monaco to Saint-Tropez), the Alps (Courchevel, Méribel, Megève) and Paris (essentially market premium). Always looking for opportunities for our clients, we work on two investment areas: residential luxury real estate (properties, vineyards, mansions, land, etc.) commercial real estate (empty office buildings or yield, hotel properties, land, etc.) "

Target Market(s)

High foreign end customers. corporate and private.

Industry/Entity Type

Real Estate

Contact Information for Business Card

LOGO
baseline
Laurent Dufossé
+33(0)6.41.57.09.64
ld@brandhill-demo.fr
www.brandhill-demo.fr

Font styles to use
Serif

Colors
cedeed
0255a3
3277b5
85abd2
85cae6
34a7d7
0792cd
cfdeed
1b1b1b

Requirements
Must have
• see description

```html
<!DOCTYPE html>
<html lang="en">
<head>
<meta charset="utf-8">
<title>BRANDHILL business card</title>
<link href="https://fonts.googleapis.com/css2?family=Questrial&family=Open+Sans:wght@400;600;700&display=swap" rel="stylesheet">
<style>
  :root {
    --page: #8e8e8e;
    --card-white: #ffffff;
    --brand-blue: #0b3a94;
    --brand-blue-deep: #09348a;
    --pattern-blue: #10419c;
    --name-blue: #0a3a8c;
    --logo-grey: #6a6a6a;
    --text-grey: #777777;
    --text-dark: #3a3a3a;
    --faint: #eef1f5;
    --pale-blue: #e3eaf4;
    --on-blue: #e4ebf7;
  }
  * { box-sizing: border-box; margin: 0; padding: 0; }
  html, body { width: 1105px; height: 1200px; overflow: hidden; }
  body { background: var(--page); position: relative; font-family: 'Open Sans', sans-serif; }

  .card { position: absolute; left: 196px; width: 720px; height: 412px; overflow: hidden; }
  .card--front { top: 146px; background: var(--card-white); }
  .card--back { top: 602px; background: var(--brand-blue); }

  .wordmark { position: absolute; display: inline-block; text-align: right; font-family: 'Questrial', sans-serif; }
  .wordmark__name { display: block; font-size: 54px; line-height: 1; letter-spacing: 4px; }
  .wordmark__baseline { display: block; font-size: 17px; line-height: 1; margin-top: 6px; letter-spacing: 0.6px; }

  .card--front .wordmark { left: 48px; top: 76px; }
  .card--front .wordmark__name { color: var(--logo-grey); }
  .card--front .wordmark__baseline { color: var(--brand-blue); }

  .front-accent { position: absolute; right: 0; top: 0; width: 720px; height: 412px; }

  .contact { position: absolute; left: 47px; top: 238px; }
  .contact__role { font-size: 19px; color: var(--text-grey); line-height: 1; margin-bottom: 14px; }
  .contact__line { font-size: 17px; color: var(--text-dark); line-height: 1; margin-bottom: 11px; }
  .contact__web { font-size: 18px; color: var(--brand-blue); letter-spacing: 2.4px; line-height: 1; margin-top: 10px; }

  .person { position: absolute; left: 427px; width: 240px; top: 290px; text-align: center; }
  .person__name { font-size: 24px; font-weight: 700; color: var(--name-blue); line-height: 1; }
  .person__title { font-size: 16px; color: var(--text-grey); margin-top: 6px; line-height: 1; }

  .back-pattern { position: absolute; inset: 0; width: 720px; height: 412px; }
  .card--back .wordmark { left: 50%; top: 174px; transform: translateX(-50%); }
  .card--back .wordmark__name { color: #ffffff; }
  .card--back .wordmark__baseline { color: #ffffff; }
  .back-web { position: absolute; left: 0; right: 0; top: 334px; text-align: center; font-size: 18px; letter-spacing: 5.5px; color: var(--on-blue); line-height: 1; }
</style>
</head>
<body>
  <section class="card card--front" aria-label="Business card front">
    <svg class="front-accent" viewBox="0 0 720 412" aria-hidden="true">
      <circle cx="572" cy="206" r="196" fill="none" stroke="var(--faint)" stroke-width="16"/>
      <rect x="605" y="48" width="115" height="268" fill="var(--pale-blue)"/>
    </svg>
    <div class="wordmark">
      <span class="wordmark__name">BRANDHILL</span>
      <span class="wordmark__baseline">real estate family office</span>
    </div>
    <div class="contact">
      <p class="contact__role">Real estate family office</p>
      <p class="contact__line">+33(0)6.41.57.09.64</p>
      <p class="contact__line">ld@brandhill-demo.fr</p>
      <p class="contact__web">www.brandhill-demo.fr</p>
    </div>
    <div class="person">
      <p class="person__name">Laurent Dufossé</p>
      <p class="person__title">CEO</p>
    </div>
  </section>

  <section class="card card--back" aria-label="Business card back">
    <svg class="back-pattern" viewBox="0 0 720 412" role="img" aria-label="Subtle repeating tone-on-tone pattern across the blue background">
      <defs>
        <linearGradient id="backTone" x1="0" y1="0" x2="1" y2="1">
          <stop offset="0" stop-color="var(--pattern-blue)"/>
          <stop offset="1" stop-color="var(--brand-blue-deep)"/>
        </linearGradient>
      </defs>
      <rect width="720" height="412" fill="url(#backTone)"/>
    </svg>
    <div class="wordmark">
      <span class="wordmark__name">BRANDHILL</span>
      <span class="wordmark__baseline">real estate family office</span>
    </div>
    <p class="back-web">www.brandhill-demo.fr</p>
  </section>
</body>
</html>
```